Corvane Nightclub Flyer (Updated)

Flyer for facebook, square is fine, or rectangular. Here is the text:
CORVANE
Nightclub + Lounge
presents

HALO THURSDAY
Nov 29 2018

CLUB FLOOR:
GLEN B2B ROBBY
FREDERICK TALAVERO

LOUNGE:
CARL B2B SKY PILOT
ROCKET JULES

Powered by KESTA Acoustics
4217 6th Street 21+ 9pm-2am
corvanevenuehall.com for VIP booth inquiries

Target Market(s)

Nightclub

Industry/Entity Type

Night Club

Font styles to use
Sans Serif

Colors

Designer to choose colors to be used in the design.

Requirements
Must have
• All the text listed, and plz keep the theme of the attached files. We want to stay consistent with the Corvane brand
Nice to have
• Try to stay with the theme from the attachments
Should not have
• Dont' stray to far from the general theme we have from the attachments

```html
<!DOCTYPE html>
<html lang="en">
<head>
<meta charset="utf-8">
<title>Corvane Nightclub – Halo Thursday Flyer</title>
<link href="https://fonts.googleapis.com/css2?family=Bodoni+Moda:wght@500;600&family=Montserrat:wght@500;600&display=swap" rel="stylesheet">
<style>
  :root {
    --slate: #3a4a63;
    --ink: #000000;
    --paper: #ffffff;
    --gold: #a8865a;
    --gold-light: #d7b27a;
    --gold-dark: #8a6a3f;
    --text-on-dark: #ffffff;
    --text-on-light: #3b3b3b;
    --muted-on-light: #777777;
  }
  * { margin: 0; padding: 0; box-sizing: border-box; }
  html, body { width: 1200px; height: 640px; overflow: hidden; }
  body {
    background: var(--slate);
    position: relative;
    font-family: "Montserrat", sans-serif;
  }
  .flyer {
    position: absolute;
    top: 61px;
    width: 516px;
    height: 516px;
    overflow: hidden;
    text-align: center;
  }
  .flyer--dark { left: 78px; background: var(--ink); color: var(--text-on-dark); }
  .flyer--light { left: 616px; background: var(--paper); color: var(--text-on-light); }

  .flyer > * { position: absolute; left: 0; right: 0; }

  .venue-name {
    top: 82px;
    font-family: "Bodoni Moda", serif;
    font-weight: 500;
    font-size: 36px;
    line-height: 40px;
    letter-spacing: 1px;
  }
  .flyer--dark .venue-name { color: var(--text-on-dark); }
  .flyer--light .venue-name { color: #444444; }

  .venue-tagline {
    top: 124px;
    font-size: 7.5px;
    line-height: 10px;
    letter-spacing: 1.6px;
  }
  .flyer--dark .venue-tagline,
  .flyer--dark .presents { color: var(--text-on-dark); }
  .flyer--light .venue-tagline { color: var(--muted-on-light); }

  .presents {
    top: 148px;
    font-size: 9px;
    line-height: 12px;
    letter-spacing: 1.6px;
  }

  .gold-rule {
    left: 98px; right: 98px;
    height: 3px;
    background: linear-gradient(90deg, transparent, var(--gold-dark) 20%, var(--gold-light) 50%, var(--gold-dark) 80%, transparent);
  }
  .gold-rule--top { top: 176px; }
  .gold-rule--bottom { top: 253px; }

  .event-title {
    top: 183px;
    font-family: "Bodoni Moda", serif;
    font-weight: 600;
    font-size: 37px;
    line-height: 46px;
    color: var(--gold);
    letter-spacing: 0;
  }

  .event-date {
    top: 229px;
    font-size: 13px;
    line-height: 16px;
    font-weight: 600;
    letter-spacing: 3.6px;
  }

  .room-label {
    left: 50%;
    width: 114px;
    margin-left: -57px;
    height: 16px;
    line-height: 16px;
    font-size: 9.5px;
    font-weight: 500;
    letter-spacing: 2.2px;
    color: #fff8ec;
    background: linear-gradient(90deg, var(--gold-dark), var(--gold-light) 60%, var(--gold));
  }
  .room-label--club { top: 281px; }
  .room-label--lounge { top: 339px; }

  .lineup {
    font-size: 10px;
    font-weight: 600;
    line-height: 13px;
    letter-spacing: 1.8px;
  }
  .lineup--club { top: 302px; }
  .lineup--lounge { top: 359px; }

  .venue-info {
    top: 405px;
    font-size: 7px;
    line-height: 10.5px;
    letter-spacing: 1.2px;
  }
  .flyer--light .venue-info { color: #555555; }

  .ornament {
    top: 335px;
    width: 126px;
    height: 181px;
  }
  .ornament--left {
    left: 0; right: auto;
    border-radius: 0 126px 0 0 / 0 181px 0 0;
  }
  .ornament--right {
    right: 0; left: auto;
    border-radius: 126px 0 0 0 / 181px 0 0 0;
  }
  .flyer--dark .ornament--left {
    background: radial-gradient(circle at 0% 100%, #3d2d18 0%, #7a5a33 45%, #a8865a 70%, #2a1f12 100%);
  }
  .flyer--dark .ornament--right {
    background: radial-gradient(circle at 100% 100%, #3d2d18 0%, #7a5a33 45%, #a8865a 70%, #2a1f12 100%);
  }
  .flyer--light .ornament--left {
    background: radial-gradient(circle at 0% 100%, #e6c79a 0%, #f3e3c8 45%, #d9b883 70%, #f7eee0 100%);
  }
  .flyer--light .ornament--right {
    background: radial-gradient(circle at 100% 100%, #e6c79a 0%, #f3e3c8 45%, #d9b883 70%, #f7eee0 100%);
  }
</style>
</head>
<body>

<section class="flyer flyer--dark">
  <div class="venue-name">CORVANE</div>
  <div class="venue-tagline">NIGHTCLUB + LOUNGE</div>
  <div class="presents">PRESENTS</div>
  <div class="gold-rule gold-rule--top"></div>
  <h1 class="event-title">HALO THURSDAY</h1>
  <div class="event-date">NOVEMBER 29, 2018</div>
  <div class="gold-rule gold-rule--bottom"></div>
  <div class="ornament ornament--left" role="img" aria-label="Gold mandala ornament, left corner"></div>
  <div class="ornament ornament--right" role="img" aria-label="Gold mandala ornament, right corner"></div>
  <div class="room-label room-label--club">CLUB FLOOR:</div>
  <div class="lineup lineup--club">GLEN B2B ROBBY<br>FREDERICK TALAVERO</div>
  <div class="room-label room-label--lounge">LOUNGE:</div>
  <div class="lineup lineup--lounge">CARL B2B SKY PILOT<br>ROCKET JULES</div>
  <div class="venue-info">POWERED BY KESTA ACOUSTICS<br>4217 6TH STREET 21+ 9PM-2AM<br>CORVANEVENUEHALL.COM FOR VIP BOOTH INQUIRIES</div>
</section>

<section class="flyer flyer--light">
  <div class="venue-name">CORVANE</div>
  <div class="venue-tagline">NIGHTCLUB + LOUNGE</div>
  <div class="presents">PRESENTS</div>
  <div class="gold-rule gold-rule--top"></div>
  <h1 class="event-title">HALO THURSDAY</h1>
  <div class="event-date">NOVEMBER 29, 2018</div>
  <div class="gold-rule gold-rule--bottom"></div>
  <div class="ornament ornament--left" role="img" aria-label="Gold mandala ornament, left corner"></div>
  <div class="ornament ornament--right" role="img" aria-label="Gold mandala ornament, right corner"></div>
  <div class="room-label room-label--club">CLUB FLOOR:</div>
  <div class="lineup lineup--club">GLEN B2B ROBBY<br>FREDERICK TALAVERO</div>
  <div class="room-label room-label--lounge">LOUNGE:</div>
  <div class="lineup lineup--lounge">CARL B2B SKY PILOT<br>ROCKET JULES</div>
  <div class="venue-info">POWERED BY KESTA ACOUSTICS<br>4217 6TH STREET 21+ 9PM-2AM<br>CORVANEVENUEHALL.COM FOR VIP BOOTH INQUIRIES</div>
</section>

</body>
</html>
```